Elevated Vital Stride

I am a competitive bodybuilder marketing my articles and videos. I envision a picture of my physique that allows the user to click on different body parts to receive three options: free article, fee based video or fee based personalized routine. I also need a page describing meal planning options that includes videos. Would also like pages for photos and blogging.
I want to maximize site visibility. Many fitness sites use what appears to be a template like this: http://www.garyltorman.com/Gain-5-6-Pounds-Of-Muscle-Mass.html. I would be interested in incorporating some pages like that.
Updates

I have a current site at marcusdelbey.com. I have not created video content yet.I can provide my current hosting details if needed. Feel free to contact me to discuss any design questions at marcus@delbey.com or 602 555 0187.

Target Market(s)

health and fitness, weight loss, muscle gain, body building, power lifting, wellness, natural medicine

Industry/Entity Type

Marketing

Requirements
Must have
• I can provide full body photos. Want my business and personal name displayed. Possible flash design that starts small then quickly increases in size on main page?

```html
<!DOCTYPE html>
<html lang="en">
<head>
<meta charset="utf-8">
<title>Marcus Delbey — Truth in Bodybuilding</title>
<link href="https://fonts.googleapis.com/css2?family=Roboto+Condensed:wght@400;700&family=Open+Sans:wght@400;600&display=swap" rel="stylesheet">
<style>
:root{
  --bg-top:#050505;
  --bg-nav:#1c1c1c;
  --bg-tab:#2b2b2b;
  --bg-footer:#1e1e1e;
  --red:#e0140f;
  --orange:#f5a000;
  --white:#ffffff;
  --grey-text:#9a9a9a;
  --light-text:#cfcfcf;
  --link-text:#a8a8a8;
}
*{margin:0;padding:0;box-sizing:border-box}
html,body{width:1200px;height:836px;overflow:hidden;background:var(--bg-top)}
body{position:relative;font-family:"Roboto Condensed",sans-serif;color:var(--white)}
.abs{position:absolute}

.top-bar{left:0;top:0;width:1200px;height:39px;background:var(--bg-top)}
.account-link{top:14px;font-family:"Open Sans",sans-serif;font-size:7.5px;letter-spacing:-0.2px;color:var(--link-text);white-space:nowrap;line-height:1}
.search{left:820px;top:9px;width:200px;height:20px;background:#262626;border-radius:3px;font-family:"Open Sans",sans-serif;font-size:7.5px;color:#6d6d6d;padding:5px 13px}
.search svg{position:absolute;right:8px;top:4px}

.nav-bar{left:0;top:39px;width:1200px;height:81px;background:var(--bg-nav)}
.logo{left:177px;top:46px;width:239px;height:63px;border:1px solid #555;padding:3px}
.logo-inner{width:100%;height:100%;border:1px solid #444;display:flex;align-items:center;justify-content:center;font-size:36px;color:var(--grey-text);letter-spacing:-0.5px}
.home-tab{left:441px;top:39px;width:86px;height:81px;background:var(--bg-tab)}
.nav-item{top:72px;font-size:12px;font-weight:700;color:#b5b5b5;transform:translateX(-50%);white-space:nowrap}

.hero{left:0;top:120px;width:1200px;height:645px;background:radial-gradient(ellipse at 50% 40%,#6e6e6e 0%,#4a4a4a 45%,#2e2e2e 100%)}
.hero-title{left:0;width:1200px;text-align:center}
.hero-name{top:376px;font-size:54px;font-weight:700;letter-spacing:-1px}
.hero-sub{top:450px;font-size:31px;letter-spacing:-0.5px}
.hero-tag{top:494px;font-size:55px;font-weight:700;color:#8f8f8f;letter-spacing:-0.5px}
.arrow{top:326px}

.newsletter-tab{left:1162px;top:225px;width:38px;height:174px;background:var(--red);border-radius:3px 0 0 3px}
.newsletter-tab span{position:absolute;left:50%;top:50%;transform:translate(-50%,-50%) rotate(-90deg);font-size:15px;font-weight:700;white-space:nowrap}

.card{top:595px;width:274px;height:149px;background:rgba(40,40,40,.85);padding:8px}
.card-inner{position:relative;width:100%;height:100%;overflow:hidden;background:#1a1a1a}
.photo{position:absolute;top:0;height:100%}
.card-text{position:absolute}
.card-title{font-size:20px;line-height:1.1}
.red{color:var(--red)}
.orange{color:var(--orange)}
.card-body{font-family:"Open Sans",sans-serif;font-size:9.5px;line-height:1.65;color:#8c8c8c;margin-top:6px}

.footer{left:0;top:765px;width:1200px;height:71px;background:var(--bg-footer)}
.footer-link{top:784px;font-family:"Open Sans",sans-serif;font-size:7.5px;letter-spacing:-0.2px;color:var(--light-text);white-space:nowrap;line-height:1}
.copyright{left:185px;top:806px;font-family:"Open Sans",sans-serif;font-size:7.5px;letter-spacing:-0.2px;color:var(--light-text)}
.social-label{left:800px;top:784px;width:119px;text-align:right;font-family:"Open Sans",sans-serif;font-size:7.5px;letter-spacing:-0.2px;line-height:1.9;color:var(--light-text)}
.social{top:785px}
</style>
</head>
<body>

<div class="abs top-bar"></div>
<nav aria-label="Account">
  <span class="abs account-link" style="left:476px">MY ACCOUNT</span>
  <span class="abs account-link" style="left:549px">|</span>
  <span class="abs account-link" style="left:568px">LOGIN</span>
  <span class="abs account-link" style="left:613px">|</span>
  <span class="abs account-link" style="left:632px">REGISTER</span>
  <span class="abs account-link" style="left:688px">|</span>
  <span class="abs account-link" style="left:707px">YOUR CART IS : 0 ITEMS</span>
</nav>
<div class="abs search">SEARCH :
  <svg width="13" height="12" viewBox="0 0 13 12"><circle cx="5" cy="5" r="3.5" fill="none" stroke="#777" stroke-width="1.5"/><line x1="7.5" y1="7.5" x2="12" y2="11" stroke="#777" stroke-width="2"/></svg>
</div>

<div class="abs nav-bar"></div>
<div class="abs logo"><div class="logo-inner">MARCUSDELBEY</div></div>
<div class="abs home-tab"></div>
<span class="abs nav-item" style="left:483px">HOME</span>
<span class="abs nav-item" style="left:588px">MEAL PLANNING</span>
<span class="abs nav-item" style="left:695px">VIDEOS</span>
<span class="abs nav-item" style="left:786px">GALLERY</span>
<span class="abs nav-item" style="left:886px">WORKOUTS</span>
<span class="abs nav-item" style="left:987px">ARTICLES</span>

<section class="abs hero" role="img" aria-label="Black and white photo of a bodybuilder seen from behind in a double biceps pose"></section>
<svg class="abs arrow" style="left:129px" width="44" height="44" viewBox="0 0 44 44"><circle cx="22" cy="22" r="20" fill="none" stroke="#555" stroke-width="2"/><path d="M27 12 L13 22 L27 32 L23 22 Z" fill="#555"/></svg>
<svg class="abs arrow" style="left:1019px" width="44" height="44" viewBox="0 0 44 44"><circle cx="22" cy="22" r="20" fill="none" stroke="#555" stroke-width="2"/><path d="M17 12 L31 22 L17 32 L21 22 Z" fill="#555"/></svg>
<h1 class="abs hero-title hero-name">MARCUS DELBEY</h1>
<p class="abs hero-title hero-sub">AM A BODY BUILDER AND I MARKET MY ARTICLES AND VIDEOS</p>
<p class="abs hero-title hero-tag">TRUTH IN BODYBUILDING</p>

<div class="abs newsletter-tab"><span>NEWSLETTER SIGNUP</span></div>

<article class="abs card" style="left:180px">
  <div class="card-inner">
    <div class="photo" style="left:0;width:120px;background:linear-gradient(135deg,#d27a2e,#8a3f12 60%,#2a1408)" role="img" aria-label="Bodybuilder posing with arms behind head"></div>
    <div class="card-text" style="left:124px;top:23px">
      <div class="card-title">IAM A<br><span class="red">BODY BUILDE</span></div>
      <p class="card-body">As a lifelong veteran of<br>competitive bodybuilding and<br>powerlifting</p>
    </div>
  </div>
</article>

<article class="abs card" style="left:463px">
  <div class="card-inner">
    <div class="photo" style="left:0;width:100%;background:radial-gradient(ellipse at 50% 40%,#b0562a,#6e2a12 60%,#3a1608)" role="img" aria-label="Close-up of a muscular torso"></div>
    <div class="card-text" style="left:0;width:100%;top:38px;text-align:center">
      <div class="card-title red" style="font-size:25px;font-weight:700">MEAL PLANNING</div>
      <div style="font-size:15px;line-height:1.3;margin-top:6px">CLICK HERE TO BUY OUR MEAL<br>PLANNING</div>
    </div>
  </div>
</article>

<article class="abs card" style="left:746px">
  <div class="card-inner">
    <div class="photo" style="left:0;width:100%;background:linear-gradient(90deg,#2a1608,#9a4e1c 25%,#7a3a14 55%,#241008)" role="img" aria-label="Three bodybuilders posing on a competition stage"></div>
    <div class="card-text" style="left:146px;top:29px">
      <div class="card-title">VIDEOS<br><span class="red">FOR SALE</span></div>
      <div style="font-size:12px;margin-top:5px"><span class="orange">CLICK HERE</span> TO</div>
      <div style="font-size:15px">BUY OUR VIDEOS</div>
    </div>
  </div>
</article>

<footer class="abs footer"></footer>
<nav aria-label="Footer">
  <span class="abs footer-link" style="left:185px">HOME</span>
  <span class="abs footer-link" style="left:222px">|</span>
  <span class="abs footer-link" style="left:238px">MEAL PLANNING</span>
  <span class="abs footer-link" style="left:314px">|</span>
  <span class="abs footer-link" style="left:330px">VIDEOS</span>
  <span class="abs footer-link" style="left:371px">|</span>
  <span class="abs footer-link" style="left:387px">GALLERY</span>
  <span class="abs footer-link" style="left:435px">|</span>
  <span class="abs footer-link" style="left:453px">WORKOUTS</span>
  <span class="abs footer-link" style="left:509px">|</span>
  <span class="abs footer-link" style="left:526px">ARTICLES</span>
</nav>
<p class="abs copyright">COPYRIGHTS © 2013. MARCUS DELBEY. ALL RIGHTS RESERVED.</p>
<p class="abs social-label">CONNECT TO<br>OUR SOCAIL NETWORK :</p>
<svg class="abs social" style="left:929px" width="90" height="27" viewBox="0 0 90 27" role="img" aria-label="Social network links">
  <circle cx="13" cy="13.5" r="13" fill="#3a62a8"/>
  <circle cx="44" cy="13.5" r="13" fill="#2aa9e0"/>
  <circle cx="75" cy="13.5" r="13" fill="#d4211f"/>
</svg>

</body>
</html>
```